New eyelid plastic surgery office needs a business card design-Eyelid Specialists of the Brenwick

I recently used DraftHarbor for my logo design and was very pleased with creativity and results. It was a difficult decision for me. Now I would like to create a business card based on this logo, which I will attach.

The text should be easily legible as some of my patients have difficulty seeing, but I would like a subtle, sophisticated artistry also evident to make the card memorable. Would like the card based on a similar color scheme as the logo but the inverse or other complementary colors may prove interesting

A good question was asked...my concern about my visually impaired patients was really my desire to avoid italicized or calligraphic type fonts that may be hard to read. Standard font size for a business card would be fine. Thanks!

Thank you so much for the great work so far. I wanted to give you my particular contact information to see if that would change the look of the cards. Martin Holloway, MD Address: 2871 Larkspur Lane, Suite 215 Wilmington, NC 39512 Phone: 555-382-1946 Fax: 555-382-1947 Website: www.brenwickliddesign.example Please delete the email slot from the card. Thanks so much!

Reason: Last minute consideration. So many great revisions right now!

Plastic

```html
<!DOCTYPE html>
<html lang="en">
<head>
<meta charset="utf-8">
<title>Eyelid Specialists of the Brenwick – Business Card</title>
<link rel="stylesheet" href="https://fonts.googleapis.com/css2?family=Marcellus&family=Cinzel:wght@600&family=Questrial&display=swap">
<style>
  :root {
    --backdrop: #d4d4d4;
    --brand-blue: #2d4897;
    --card-black-top: #1c1c1c;
    --card-black-bottom: #000000;
    --card-white-top: #ffffff;
    --card-white-bottom: #e4e4e4;
    --ink: #2b2b2b;
    --strip-gray: #c6c6c6;
    --on-blue: #ffffff;
  }
  html, body {
    margin: 0;
    padding: 0;
    width: 1200px;
    height: 1200px;
    overflow: hidden;
    background: var(--backdrop);
  }
  .canvas {
    position: relative;
    width: 1200px;
    height: 1200px;
  }
  .card {
    position: absolute;
    left: 273px;
    width: 654px;
    height: 363px;
    overflow: hidden;
  }
  .card--front {
    top: 203px;
    background: linear-gradient(to bottom, var(--card-black-top), var(--card-black-bottom));
  }
  .card--back {
    top: 621px;
    height: 364px;
    background: linear-gradient(to bottom, var(--card-white-top), var(--card-white-bottom));
  }
  .wordmark {
    position: absolute;
    left: 0;
    width: 100%;
    margin: 0;
    text-align: center;
    font-family: "Marcellus", serif;
    font-weight: 400;
    color: var(--brand-blue);
    line-height: 1;
    text-transform: uppercase;
  }
  .wordmark__main {
    display: block;
    font-size: 41px;
    letter-spacing: 0.3px;
  }
  .wordmark__sub {
    display: block;
    font-size: 21px;
    letter-spacing: 0.5px;
    margin-top: 6px;
  }
  .card--front .wordmark { top: 151px; }
  .card--back .wordmark { top: 57px; }
  .tagline {
    position: absolute;
    top: 146px;
    left: 0;
    width: 100%;
    margin: 0;
    text-align: center;
    font-family: "Questrial", sans-serif;
    font-style: italic;
    font-size: 11px;
    letter-spacing: 2px;
    color: var(--ink);
  }
  .physician {
    position: absolute;
    top: 192px;
    left: 0;
    width: 100%;
    margin: 0;
    text-align: center;
    font-family: "Cinzel", serif;
    font-weight: 600;
    font-size: 18px;
    letter-spacing: 4px;
    color: var(--ink);
  }
  .address, .contact {
    position: absolute;
    font-family: "Questrial", sans-serif;
    font-size: 15px;
    letter-spacing: 1.2px;
    color: var(--ink);
    line-height: 30px;
    margin: 0;
  }
  .address { top: 257px; left: 51px; }
  .contact { top: 255px; left: 434px; list-style: none; padding: 0; }
  .contact li { display: flex; align-items: center; }
  .contact svg { width: 20px; height: 18px; margin-right: 24px; }
  .strip-gray {
    position: absolute;
    left: 0;
    bottom: 0;
    width: 330px;
    height: 16px;
    background: var(--strip-gray);
  }
  .strip-web {
    position: absolute;
    right: 0;
    bottom: 0;
    width: 338px;
    height: 27px;
    background: var(--brand-blue);
    border-top-left-radius: 16px;
    font-family: "Questrial", sans-serif;
    font-size: 14px;
    letter-spacing: 1.2px;
    color: var(--on-blue);
    line-height: 25px;
    padding-left: 31px;
    box-sizing: border-box;
    white-space: nowrap;
  }
</style>
</head>
<body>
<main class="canvas">
  <section class="card card--front" aria-label="Card front">
    <p class="wordmark">
      <span class="wordmark__main">Eyelid Specialists</span>
      <span class="wordmark__sub">of the Brenwick</span>
    </p>
  </section>

  <section class="card card--back" aria-label="Card back">
    <p class="wordmark">
      <span class="wordmark__main">Eyelid Specialists</span>
      <span class="wordmark__sub">of the Brenwick</span>
    </p>
    <p class="tagline">Specializing in Eyelid, Lacrimal, and Orbital Surgery</p>
    <p class="physician">Martin Holloway, MD</p>
    <p class="address">2871 Larkspur Lane, Suite 215<br>Kellerton, North Delmara 39512</p>
    <ul class="contact">
      <li>
        <svg viewBox="0 0 20 18" aria-label="Phone">
          <path d="M2 6 Q10 0 18 6 L16 8 L13 6 L13 4 Q10 3 7 4 L7 6 L4 8 Z" fill="#2d4897"/>
          <path d="M5 9 L15 9 L17 16 L3 16 Z" fill="#2d4897"/>
          <circle cx="10" cy="12.5" r="2" fill="#fff"/>
        </svg>
        (555) 382-1946
      </li>
      <li>
        <svg viewBox="0 0 20 18" aria-label="Fax">
          <rect x="5" y="1" width="10" height="5" fill="none" stroke="#2d4897" stroke-width="1.8"/>
          <rect x="2" y="6" width="16" height="7" rx="1.5" fill="#2d4897"/>
          <rect x="5" y="11" width="10" height="6" fill="#fff" stroke="#2d4897" stroke-width="1.8"/>
        </svg>
        (555) 382-1947
      </li>
    </ul>
    <div class="strip-gray"></div>
    <div class="strip-web">www.brenwickliddesign.example</div>
  </section>
</main>
</body>
</html>
```